Waterproofing Construction company needs letterhead

I need a letterhead design for a commercial waterproofing construction company. We would like to see designs that are contemporary, clean, sleek and use our logo. Our current design is dated. I would also like a cover page (see example) that goes with our letterhead. I would like for the footer to have our address, website, and phone number

Target Market(s)

Customers, potential customers.

Font styles to use
Sans Serif

Requirements
Must have
• logo, website, address, phone numbers, only our colors, tahoma font
• PMS: 295C PMS: 2995C
• CMYK: 100/84/36/39 CMYK: 80/12/1/0
• RGB: 16/44/82 RGB: 0/167/224
• HEX#: #102C52 HEX#: #00A7E0
• Black & White: 100% Black & White: 32%
• Gray Scale: 90% Gray Scale: 32%
Nice to have
• Our "icon" logo attached would be nice somewhere on the page.

```html
<!DOCTYPE html>
<html lang="en">
<head>
<meta charset="utf-8">
<title>Tidewell Letterhead</title>
<link href="https://fonts.googleapis.com/css2?family=Noto+Sans:wght@400;700&display=swap" rel="stylesheet">
<style>
  :root {
    --navy: #102C52;
    --sky: #00A7E0;
    --ink: #111111;
    --paper: #F4F4F4;
    --backdrop: #E6EBF0;
  }
  * { margin: 0; padding: 0; box-sizing: border-box; }
  html, body {
    width: 1200px; height: 1158px; overflow: hidden;
    background: var(--backdrop);
    font-family: Tahoma, "Noto Sans", sans-serif;
    color: var(--ink);
  }
  .letterhead {
    position: absolute; left: 208px; top: 20px;
    width: 785px; height: 1118px;
    background: var(--paper);
    box-shadow: 0 10px 30px rgba(16,44,82,.18);
    overflow: hidden;
  }
  .edge-band {
    position: absolute; right: 0; top: 0;
    width: 40px; height: 1118px;
    background: var(--navy);
  }
  .brand {
    position: absolute; right: 95px; top: 38px;
    text-align: right; color: var(--navy);
  }
  .brand-name {
    font-size: 74px; font-weight: 700; line-height: 1; letter-spacing: -1px;
  }
  .brand-tagline {
    margin-top: 10px; font-size: 16px; letter-spacing: .2px;
    display: flex; align-items: center; justify-content: flex-end; gap: 6px;
  }
  .brand-dot { width: 6px; height: 6px; border-radius: 50%; background: var(--sky); display: inline-block; }
  .recipient { position: absolute; left: 53px; top: 212px; }
  .recipient-to { font-size: 18px; margin-bottom: 18px; }
  .recipient-title { font-size: 18px; line-height: 1.1; }
  .recipient-company { font-size: 14px; }
  .letter-body {
    position: absolute; left: 53px; top: 366px; width: 637px;
    font-size: 10.8px; line-height: 14.5px; letter-spacing: -0.15px;
    text-align: justify;
  }
  .letter-body p + p { margin-top: 14.5px; }
  .signature {
    position: absolute; left: 480px; top: 850px; width: 210px; height: 42px;
    background: linear-gradient(90deg, rgba(17,17,17,.05), rgba(17,17,17,.12));
    border-radius: 3px;
  }
  .footer-mark {
    position: absolute; left: 60px; top: 1024px; width: 52px; height: 52px;
    background: var(--sky);
  }
  .footer-contact {
    position: absolute; right: 95px; top: 1023px;
    text-align: right; font-size: 15px; line-height: 19.5px;
  }
  .footer-contact strong { font-weight: 700; }
</style>
</head>
<body>
  <main class="letterhead">
    <div class="edge-band" aria-hidden="true"></div>

    <header class="brand">
      <div class="brand-name">TIDEWELL</div>
      <div class="brand-tagline">WATERPROOFING <span class="brand-dot"></span> RESTORATION</div>
    </header>

    <section class="recipient">
      <p class="recipient-to">To</p>
      <p class="recipient-title">General Manager</p>
      <p class="recipient-company">Company Name</p>
    </section>

    <article class="letter-body">
      <p>Lorem ipsum dolor sit amet, consectetur adipiscing elit, sed do eiusmod tempor incididunt ut labore et dolore magna aliqua. Vitae ultricies leo integer malesuada nunc vel. Aenean vel elit scelerisque mauris. Elementum sagittis vitae et leo duis ut diam quam nulla. Tellus at urna condimentum mattis pellentesque id nibh tortor id. Felis donec et odio pellentesque diam volutpat commodo sed egestas. Tincidunt eget nullam non nisi est. Porttitor massa id neque aliquam vestibulum. Risus quis varius quam quisque id diam vel. Non arcu risus quis varius quam quisque id diam. Sit amet consectetur adipiscing elit pellentesque habitant morbi tristique.</p>
      <p>Nec nam aliquam sem et tortor. Lacinia quis vel eros donec ac. Auctor eu augue ut lectus arcu. Urna id volutpat lacus laoreet non curabitur gravida arcu. Pretium vulputate sapien nec sagittis aliquam. Egestas egestas fringilla phasellus faucibus scelerisque eleifend donec. Sagittis id consectetur purus ut faucibus pulvinar elementum integer. Egestas maecenas pharetra convallis posuere morbi leo urna molestie at. Nibh nisl condimentum id venenatis a condimentum vitae sapien pellentesque. Augue ut lectus arcu bibendum at varius vel pharetra. Lorem ipsum dolor sit amet consectetur. Metus aliquam eleifend mi in nulla posuere.</p>
      <p>Aliquet porttitor lacus luctus accumsan tortor posuere ac ut. Ullamcorper morbi tincidunt ornare massa eget egestas purus viverra. Nulla posuere sollicitudin aliquam ultrices sagittis orci a scelerisque purus. Libero enim sed faucibus turpis in eu mi. Vel pharetra vel turpis nunc eget. Maecenas accumsan lacus vel facilisis volutpat est velit egestas dui. Pretium aenean pharetra magna ac placerat vestibulum. Amet est placerat in egestas erat imperdiet sed euismod nisi. Scelerisque in dictum non consectetur a erat nam. Id cursus metus aliquam eleifend mi in. Viverra mauris in aliquam sem fringilla ut morbi tincidunt. Enim ut tellus elementum sagittis vitae et leo duis ut. Ultricies tristique nulla aliquet enim.</p>
      <p>Tincidunt id aliquet risus feugiat in. Orci eu lobortis elementum nibh tellus molestie nunc non blandit. Blandit cursus risus at ultrices mi tempus imperdiet nulla malesuada. Erat imperdiet sed euismod nisi porta lorem mollis aliquam ut. Non enim praesent elementum facilisis leo vel fringilla. Urna neque viverra justo nec. Felis imperdiet proin fermentum leo. Auctor eu augue ut lectus arcu bibendum at varius. Molestie ac feugiat sed lectus vestibulum mattis ullamcorper velit sed. Laoreet suspendisse interdum consectetur libero id. Pharetra diam sit amet nisl suscipit. Scelerisque fermentum dui faucibus in ornare quam viverra. Ullamcorper morbi tincidunt ornare massa eget egestas. Metus vulputate eu scelerisque felis imperdiet proin fermentum.</p>
    </article>

    <div class="signature" role="img" aria-label="Handwritten signature placeholder"></div>

    <footer>
      <div class="footer-mark" aria-hidden="true"></div>
      <div class="footer-contact">
        <p><strong>www.tidewellwp.com</strong></p>
        <p>PO Box 460 | Fairview, NC 28730 | <strong>O</strong>: (877) 555-0142 &nbsp;| &nbsp;<strong>F</strong>: (919) 555-0187</p>
        <p><strong>North Carolina &nbsp;| &nbsp;South Carolina &nbsp;| &nbsp;Virginia</strong></p>
      </div>
    </footer>
  </main>
</body>
</html>
```